Veterinarian specialized in Equine (horse) sports medicine needs logo and stationary design!

New veterinary clinic only focused on horses needs logo and stationary designs. The clinic works with sport horses including jumping horses, dressage horses and polo horses (all disciplines you can find online. No racing horses). Name of clinic is StrideCare and is based in Mexico City where there is a large and elite clientele of sports horses. My main focus is orthopedics and rehabilitation.
I think logo should include horse(s), especially if they are performing a sport (like jumping, etc).

Target Market(s)

Elite horse-owners of sport horses.

Industry/Entity Type

Horseback Riding

Requirements
Must have
• Great Logo! I like bold and bright colors (no pastels), but with a professional tone.

```html
<!DOCTYPE html>
<html lang="en">
<head>
<meta charset="utf-8">
<title>StrideCare Stationery</title>
<link href="https://fonts.googleapis.com/css2?family=Cinzel:wght@400&family=Open+Sans:wght@400;700&display=swap" rel="stylesheet">
<style>
:root{
  --bg:#d6d7d9;
  --green:#8bc540;
  --green-dark:#78b033;
  --grey:#6d6e70;
  --grey-flap:#7c7d7f;
  --paper:#ffffff;
  --ink:#3a3a3a;
}
*{box-sizing:border-box;margin:0;padding:0}
html,body{width:1200px;height:1200px;overflow:hidden;background:var(--bg)}
body{position:relative;font-family:"Open Sans",sans-serif;color:var(--ink)}
.item{position:absolute}
.sheet{background:var(--paper)}
.green{background:var(--green)}

/* wordmark */
.brand{display:flex;align-items:center;justify-content:center;gap:.35em;font-family:"Cinzel",serif;font-weight:400;color:var(--grey);white-space:nowrap;line-height:1}
.brand .dot{width:.55em;height:.55em;border-radius:50%;background:var(--green);flex:none}
.brand.light{color:#fff}
.brand.light .dot{background:#fff}
.rule{height:2px;background:var(--green)}
.light-rule{background:#fff}

.hero{left:0;top:150px;width:1200px;font-size:78px}
.hero-rule{left:443px;top:262px;width:341px;height:3px}

/* folder */
.folder-side{left:53px;top:320px}
.folder-left{left:102px;top:320px;width:248px;height:341px}
.folder-right{left:350px;top:320px;width:249px;height:341px}
.folder-right .brand{position:absolute;left:0;right:0;top:160px;font-size:26px}
.folder-right .rule{position:absolute;left:66px;width:116px;top:200px;height:1.5px}
.contact-row{position:absolute;left:0;right:0;bottom:18px;display:flex;justify-content:center;gap:18px;font-size:4px;color:#fff}

/* letterhead */
.letterhead{left:608px;top:320px;width:241px;height:341px}
.letterhead .brand{margin-top:22px;font-size:13px}
.small{font-size:4px;text-align:center;color:#444}
.lh-head{display:flex;justify-content:space-between;margin:28px 34px 0;font-size:4.4px;font-weight:700}
.lh-head span.sub{display:block;font-weight:400;font-size:3px}
.lh-body{margin:18px 34px 0;font-size:3.6px;line-height:1.45;color:#333}
.lh-body p{margin-bottom:6px}
.lh-sign{position:absolute;right:34px;top:272px;text-align:right;font-size:4.4px;font-weight:700}
.lh-sign span{display:block;font-weight:400;font-size:3px}
.lh-sign i{display:block;margin-top:10px;border-bottom:1px solid #333;width:38px;margin-left:auto}
.lh-foot{position:absolute;left:0;right:0;bottom:8px;display:flex;justify-content:space-around;font-size:3.6px}
.lh-bar{position:absolute;left:0;right:0;bottom:0;height:4px;background:var(--green)}

/* cards */
.card-front{left:833px;top:439px;width:130px;height:74px;display:flex;align-items:center;justify-content:center;font-size:11px}
.card-back{left:833px;top:533px;width:130px;height:73px}
.card-back .brand{position:absolute;right:9px;top:14px;font-size:8px}
.card-back .who{position:absolute;right:9px;top:33px;text-align:right;font-size:4px;font-family:"Cinzel",serif}
.card-back .who span{display:block;font-size:3px;font-style:italic}
.card-back .lines{position:absolute;right:9px;top:47px;text-align:right;font-size:2.6px;line-height:1.5}

/* notepad */
.notepad{left:980px;top:378px;width:181px;height:250px}
.notepad .brand{position:absolute;left:0;right:0;top:125px;font-size:18px}
.notepad .rule{position:absolute;left:50px;width:82px;top:148px;height:1.2px}
.notepad .url{position:absolute;left:0;right:0;bottom:8px;text-align:center;font-size:3.6px;color:#fff}

/* blank sheet */
.plain-sheet{left:64px;top:751px;width:245px;height:346px}
.plain-sheet .brand{position:absolute;left:25px;top:45px;font-size:15px;justify-content:flex-start}
.plain-sheet .addr{position:absolute;left:26px;top:65px;font-size:4.4px}

/* open envelope */
.envelope-open{left:253px;top:768px;width:244px;height:346px}
.envelope-open .flap{position:absolute;left:0;right:0;top:0;height:41px}
.envelope-open .addr{position:absolute;left:24px;bottom:30px;font-size:4.2px;line-height:1.35}

/* notebook */
.notebook{left:532px;top:698px;width:230px;height:325px}
.notebook .brand{position:absolute;left:0;right:0;top:148px;font-size:22px}
.notebook .rule{position:absolute;left:68px;width:96px;top:177px;height:1.5px}
.notebook .addr{position:absolute;right:14px;bottom:16px;text-align:right;font-size:4.4px;line-height:1.4;color:#fff}
.rings{left:516px;top:712px}

/* window envelope */
.dl-front{left:797px;top:737px;width:331px;height:165px}
.dl-front .window{position:absolute;left:25px;top:58px;width:111px;height:55px;border-radius:10px;background:#f4f4f4}
.dl-front .brand{position:absolute;right:18px;top:48px;font-size:18px}
.dl-front .rule{position:absolute;right:18px;width:78px;top:68px;height:1.2px}
.dl-front .addr{position:absolute;right:18px;top:120px;text-align:right;font-size:6px;line-height:1.35;color:#fff}

/* envelope back */
.dl-back{left:797px;top:932px;width:331px;height:165px}
.dl-back .flap{position:absolute;left:0;right:0;top:0;height:55px}
.dl-back .brand{position:absolute;right:28px;top:116px;font-size:17px}
.dl-back .rule{position:absolute;right:28px;width:76px;top:135px;height:1.2px}
</style>
</head>
<body>

<div class="item brand hero"><span class="dot"></span>StrideCare</div>
<div class="item rule hero-rule"></div>

<!-- folder -->
<svg class="item folder-side" width="300" height="400" viewBox="0 0 300 400" aria-hidden="true">
  <polygon points="0,26 49,0 49,341 0,341" fill="var(--grey-flap)"/>
  <polygon points="49,341 297,341 250,398 49,398" fill="var(--grey-flap)"/>
</svg>
<div class="item folder-left green">
  <div class="contact-row"><span>555-210-4417</span><span>hola@stridecare.mx</span><span>www.stridecare.mx</span></div>
</div>
<div class="item folder-right sheet">
  <div class="brand"><span class="dot"></span>StrideCare</div>
  <div class="rule"></div>
</div>

<!-- letterhead -->
<div class="item letterhead sheet">
  <div class="brand"><span class="dot"></span>StrideCare</div>
  <div class="small">48 Paseo Norte, Lomas, CDMX 11000</div>
  <div class="lh-head">
    <div>Dear Mr.________<span class="sub">Designation</span><span class="sub">COMPANY NAME</span></div>
    <div>DATE:1/5/2018</div>
  </div>
  <div class="lh-body">
    <p>Thank you for trusting our team with the care of your horse. This letter confirms the plan we agreed on during the recent visit.</p>
    <p>Our orthopedic review found mild strain in the left fore. We advise two weeks of controlled walking before any return to jumping work.</p>
    <p>Rehabilitation sessions will take place at our clinic each Tuesday and Friday. Please bring recent shoeing notes and any earlier imaging results.</p>
    <p>We will send a progress report after each stage. Do not hesitate to call us with any question about the program.</p>
  </div>
  <div class="lh-sign">YOUR NAME<span>Designation</span><i></i></div>
  <div class="lh-foot"><span>555-210-4417</span><span>hola@stridecare.mx</span><span>www.stridecare.mx</span></div>
  <div class="lh-bar"></div>
</div>

<!-- business cards -->
<div class="item card-front green brand light"><span class="dot"></span>StrideCare</div>
<div class="item card-back sheet">
  <div class="brand"><span class="dot"></span>StrideCare</div>
  <div class="who">ELENA RUIZ<span>Director</span></div>
  <div class="lines">555-210-4417<br>hola@stridecare.mx<br>www.stridecare.mx<br>48 Paseo Norte, CDMX</div>
</div>

<!-- notepad -->
<svg class="item" style="left:988px;top:372px" width="168" height="14" viewBox="0 0 168 14" aria-hidden="true">
  <g stroke="var(--grey)" stroke-width="2" stroke-linecap="round">
    <line x1="4" y1="2" x2="4" y2="12"/><line x1="11" y1="2" x2="11" y2="12"/><line x1="18" y1="2" x2="18" y2="12"/><line x1="25" y1="2" x2="25" y2="12"/><line x1="32" y1="2" x2="32" y2="12"/><line x1="39" y1="2" x2="39" y2="12"/><line x1="46" y1="2" x2="46" y2="12"/><line x1="53" y1="2" x2="53" y2="12"/><line x1="60" y1="2" x2="60" y2="12"/><line x1="67" y1="2" x2="67" y2="12"/><line x1="74" y1="2" x2="74" y2="12"/><line x1="81" y1="2" x2="81" y2="12"/><line x1="88" y1="2" x2="88" y2="12"/><line x1="95" y1="2" x2="95" y2="12"/><line x1="102" y1="2" x2="102" y2="12"/><line x1="109" y1="2" x2="109" y2="12"/><line x1="116" y1="2" x2="116" y2="12"/><line x1="123" y1="2" x2="123" y2="12"/><line x1="130" y1="2" x2="130" y2="12"/><line x1="137" y1="2" x2="137" y2="12"/><line x1="144" y1="2" x2="144" y2="12"/><line x1="151" y1="2" x2="151" y2="12"/><line x1="158" y1="2" x2="158" y2="12"/><line x1="165" y1="2" x2="165" y2="12"/>
  </g>
</svg>
<div class="item notepad green">
  <div class="brand light"><span class="dot"></span>StrideCare</div>
  <div class="rule light-rule"></div>
  <div class="url">www.stridecare.mx</div>
</div>

<!-- plain sheet -->
<div class="item plain-sheet sheet">
  <div class="brand"><span class="dot"></span>StrideCare</div>
  <div class="addr">48 Paseo Norte, Lomas, CDMX 11000</div>
</div>

<!-- open envelope -->
<div class="item envelope-open sheet">
  <div class="flap green"></div>
  <div class="addr">555-210-4417<br>48 Paseo Norte, Lomas, CDMX 11000<br>www.stridecare.mx</div>
</div>

<!-- notebook -->
<div class="item notebook green">
  <div class="brand light"><span class="dot"></span>StrideCare</div>
  <div class="rule light-rule"></div>
  <div class="addr">555-210-4417<br>clinic@hoofline.mx<br>48 Paseo Norte, Lomas, CDMX 11000<br>www.hoofline.mx</div>
</div>
<svg class="item rings" width="30" height="295" viewBox="0 0 30 295" aria-hidden="true">
  <g stroke="var(--grey)" stroke-width="5" stroke-linecap="round">
    <line x1="3" y1="6" x2="26" y2="6"/><line x1="3" y1="27" x2="26" y2="27"/><line x1="3" y1="48" x2="26" y2="48"/><line x1="3" y1="69" x2="26" y2="69"/><line x1="3" y1="90" x2="26" y2="90"/><line x1="3" y1="111" x2="26" y2="111"/><line x1="3" y1="132" x2="26" y2="132"/><line x1="3" y1="153" x2="26" y2="153"/><line x1="3" y1="174" x2="26" y2="174"/><line x1="3" y1="195" x2="26" y2="195"/><line x1="3" y1="216" x2="26" y2="216"/><line x1="3" y1="237" x2="26" y2="237"/><line x1="3" y1="258" x2="26" y2="258"/><line x1="3" y1="279" x2="26" y2="279"/>
  </g>
</svg>

<!-- window envelope -->
<div class="item dl-front green">
  <div class="window"></div>
  <div class="brand light"><span class="dot"></span>StrideCare</div>
  <div class="rule light-rule"></div>
  <div class="addr">555-210-4417<br>48 Paseo Norte, Lomas, CDMX 11000<br>www.hoofline.mx</div>
</div>

<!-- envelope back -->
<div class="item dl-back sheet">
  <div class="flap green"></div>
  <div class="brand"><span class="dot"></span>StrideCare</div>
  <div class="rule"></div>
</div>

</body>
</html>
```